" Trata-se de consultório médico particular, de especialidade em gastroenterologia, cujos impressos serao utilizados como cartao de visita, receituários e envelopes. "

```html
<!DOCTYPE html>
<html lang="pt-BR">
<head>
<meta charset="utf-8">
<title>Helena Barros Vidal – Cartão de visita</title>
<link rel="stylesheet" href="https://fonts.googleapis.com/css2?family=Tenor+Sans&family=Open+Sans:wght@300;400&display=swap">
<style>
  :root {
    --page-bg: #ecebe8;
    --lavender: #9d9cd2;
    --lavender-text: #f4f3fb;
    --ink-violet: #6f6cb0;
    --ink-soft: #8583c0;
    --card-white: #ffffff;
    --mark-tint: #e4e3f3;
  }
  * { margin: 0; padding: 0; box-sizing: border-box; }
  html, body { width: 1200px; height: 1200px; overflow: hidden; }
  body {
    background: var(--page-bg);
    position: relative;
  }
  .card {
    position: absolute;
    left: 180px;
    width: 840px;
    height: 480px;
    border-radius: 44px;
    overflow: hidden;
  }
  .card--front {
    top: 110px;
    background: var(--lavender);
    color: var(--lavender-text);
    display: flex;
    flex-direction: column;
    align-items: center;
    justify-content: center;
    text-align: center;
  }
  .brand-dot {
    width: 70px;
    height: 70px;
    border-radius: 50%;
    border: 0;
    background: var(--lavender-text);
    opacity: .85;
    margin-bottom: 34px;
  }
  .front-name {
    font-family: "Tenor Sans", sans-serif;
    font-size: 44px;
    letter-spacing: 1px;
    text-transform: uppercase;
    line-height: 1;
  }
  .front-specialty {
    font-family: "Tenor Sans", sans-serif;
    font-size: 24px;
    letter-spacing: 5px;
    margin-top: 10px;
  }
  .card--back {
    top: 640px;
    background: var(--card-white);
    box-shadow: 0 0 0 1px #dddce6;
  }
  .back-decoration {
    position: absolute;
    left: 50px;
    top: 150px;
    width: 560px;
    height: 310px;
    border-radius: 40% 60% 20% 20%;
    background: radial-gradient(ellipse at 40% 60%, var(--mark-tint) 0%, rgba(228,227,243,.5) 55%, rgba(255,255,255,0) 80%);
  }
  .back-info {
    position: absolute;
    right: 52px;
    top: 48px;
    text-align: right;
    font-family: "Open Sans", sans-serif;
    font-weight: 300;
    color: var(--ink-soft);
  }
  .back-name {
    font-size: 38px;
    color: var(--ink-violet);
    line-height: 1.1;
  }
  .back-role {
    font-size: 16px;
    line-height: 1.35;
    margin-top: 6px;
  }
  .back-clinic {
    font-size: 19px;
    line-height: 1.35;
    margin-top: 58px;
  }
  .back-phone {
    font-size: 22px;
    color: var(--ink-violet);
    margin-top: 22px;
  }
  .back-address {
    font-size: 19px;
    line-height: 1.4;
    margin-top: 18px;
  }
</style>
</head>
<body>
  <section class="card card--front">
    <div class="brand-dot"></div>
    <h1 class="front-name">Helena Barros Vidal</h1>
    <p class="front-specialty">Gastroenterologia</p>
  </section>

  <section class="card card--back">
    <div class="back-decoration" role="img" aria-label="Marca da médica em grande escala, em lilás claro, como fundo decorativo"></div>
    <div class="back-info">
      <h2 class="back-name">Helena Barros Vidal</h2>
      <p class="back-role">Gastroenterologia<br>Doenças Inflamatórias Intestinais</p>
      <p class="back-clinic">Vitanova Clínica de Infusão<br>e Especialidades</p>
      <p class="back-phone">(27) 3410 2286</p>
      <p class="back-address">Rua das Acácias, 512<br>Ed. Aurora Center, G4<br>Santa Clara Vitória ES<br>CEP 29010-318</p>
    </div>
  </section>
</body>
</html>
```